Postcard Design Project

We are a small printing company specializing in envelope printing.
We market to churches and medical offices.

Industry/Entity Type

It Company

```html
<!DOCTYPE html>
<html lang="en">
<head>
<meta charset="utf-8">
<title>RJT Designs – Envelope Printing Postcard</title>
<link href="https://fonts.googleapis.com/css2?family=Nunito+Sans:wght@300;400;700;800&family=Arimo:wght@700&display=swap" rel="stylesheet">
<style>
  :root {
    --navy-deep: #2c3650;
    --navy: #3a455e;
    --slate: #7b8a9f;
    --sky-pale: #c3d4e6;
    --accent-green: #b6e03a;
    --accent-blue: #8fd3f5;
    --white: #ffffff;
    --ink: #111111;
  }
  * { margin: 0; padding: 0; box-sizing: border-box; }
  html, body { width: 1200px; height: 800px; overflow: hidden; background: var(--white); }
  .postcard {
    position: relative; width: 1200px; height: 800px; overflow: hidden;
    background: var(--white);
    font-family: "Nunito Sans", sans-serif;
  }
  .top-band {
    position: absolute; left: 0; top: 0; width: 1200px; height: 250px;
    background: linear-gradient(100deg, var(--navy-deep) 0%, #4b5773 50%, #8ea3bd 80%, var(--sky-pale) 100%);
  }
  .promo-panel {
    position: absolute; left: 0; top: 0; width: 476px; height: 674px;
    background: linear-gradient(115deg, var(--navy-deep) 0%, var(--navy) 45%, var(--slate) 100%);
  }
  .headline-band {
    position: absolute; left: 0; top: 0; width: 476px; height: 142px;
    background: rgba(30, 38, 58, 0.55);
  }
  .headline {
    position: absolute; left: 33px; top: 16px; width: 440px;
    color: var(--white);
  }
  .headline .lead { font-size: 19px; font-weight: 400; }
  .headline .brand { font-size: 33px; font-weight: 800; color: var(--accent-green); letter-spacing: -0.3px; }
  .headline .print { font-size: 49px; font-weight: 300; letter-spacing: 1px; }
  .headline .tagline { font-size: 21px; font-weight: 400; line-height: 31px; margin-top: 2px; }
  .features {
    position: absolute; left: 50px; top: 170px; list-style: none;
    color: var(--accent-blue); font-size: 26px; font-weight: 400;
  }
  .features li { height: 41px; line-height: 34px; }
  .features li::before { content: "• "; font-size: 20px; vertical-align: 2px; }
  .note {
    position: absolute; left: 286px; top: 395px; width: 180px;
    color: var(--white); font-size: 16px; line-height: 24px;
  }
  .note span { padding-left: 8px; display: block; }
  .product-shot { position: absolute; }
  .product-shot.envelopes { left: 460px; top: 0; width: 740px; height: 250px; }
  .product-shot.offering-cards { left: 0; top: 392px; width: 456px; height: 272px; }
  .postage-area {
    position: absolute; left: 977px; top: 21px; width: 200px; height: 200px;
    background: var(--white); border: 1.5px solid var(--ink);
    display: flex; align-items: center; justify-content: center; text-align: center;
    font-family: "Arimo", sans-serif; font-weight: 700; font-size: 22px; line-height: 27px; color: var(--ink);
  }
  .mail-label {
    position: absolute; font-family: "Arimo", sans-serif; font-weight: 700;
    font-size: 21px; color: var(--ink); transform: translateX(-50%);
  }
  .address-area { left: 904px; top: 431px; }
  .barcode-area { left: 607px; top: 725px; }
</style>
</head>
<body>
  <main class="postcard">
    <div class="top-band"></div>

    <svg class="product-shot envelopes" viewBox="0 0 740 250" role="img" aria-label="Product photo of printed business, dental and medical billing envelopes and a church offering envelope">
      <g transform="rotate(6 380 120)">
        <rect x="200" y="-40" width="330" height="250" fill="#f3f5f8"/>
        <rect x="200" y="195" width="330" height="12" fill="#1f8fd6"/>
      </g>
      <g transform="rotate(-14 600 90)">
        <rect x="420" y="10" width="330" height="170" fill="#fbfbfb"/>
      </g>
      <g transform="rotate(3 300 165)">
        <rect x="0" y="92" width="290" height="150" fill="#eef0f4"/>
        <rect x="0" y="214" width="290" height="12" fill="#4a3f9c"/>
        <rect x="0" y="210" width="60" height="16" fill="#1e1a4a"/>
      </g>
    </svg>

    <div class="promo-panel">
      <div class="headline-band"></div>
      <div class="headline">
        <div><span class="lead">At </span><span class="brand">RJT Designs,</span> <span class="print">PRINT</span> <span class="lead">your</span></div>
        <p class="tagline">Great-looking envelope, which stands out &amp;<br>makes people want to open your letter.</p>
      </div>
      <ul class="features">
        <li>Custom Business Envelopes</li>
        <li>Church Offering Envelopes *</li>
        <li>Medical Billing Envelopes</li>
        <li>Free Copy Changes</li>
        <li>Free Shipping</li>
      </ul>
      <p class="note">* Variety of Paper and<span>Size Options</span></p>

      <svg class="product-shot offering-cards" viewBox="0 0 456 272" role="img" aria-label="Product photo of printed church tithe and offering envelopes">
        <g transform="rotate(-13 140 110)">
          <rect x="20" y="40" width="250" height="130" fill="#d9d2c8"/>
        </g>
        <g transform="rotate(-8 110 180)">
          <rect x="-10" y="120" width="220" height="140" fill="#e3e7ee"/>
        </g>
        <g transform="rotate(-17 290 170)">
          <rect x="170" y="90" width="280" height="170" fill="#fafafa"/>
          <rect x="330" y="125" width="105" height="90" fill="none" stroke="#f08a1c" stroke-width="2"/>
        </g>
      </svg>
    </div>

    <div class="postage-area">Postage<br>Area</div>
    <p class="mail-label address-area">Address Area</p>
    <p class="mail-label barcode-area">Barcode Area</p>
  </main>
</body>
</html>
```